Photoshop Design Project

Just looking to use some existing element in emails and printed flyers for a lunch menu promo.

I am attaching a menu in progress to reference only the front page design of a chalkboard, chalk fonts, tagline of :Trade the Same Old Plate for Midday Fresh Bites. Its on the front of the menu.

I just want to drop in a photo of each on three separate pieces with description.

THe design should not be a match to the front of the menu, just utilize its elements. the design is not a lead at all, these should remain familiar with the front of the menu, but please use the elements to your design preference.

Ok to submit one layout that we can repeat, or ok to submit three different versions

Must stick with the colors though, they are brand color combo, not exact by color code, but the oranges and the browns need to stay somewhere and in some capacity.
SO menu attached, check out the front cover for inspirations, to go in email sends embedded, and to print as a flyer.

There are also three images attached they are the to be dropped into each piece, with a desciption
Updates

Reason: seems to be too many questions and I wasnt getting anywhere.. To clarify...One Design Piece (one page), three separate items, same peice, however three total. one for each product photo supplied

I moved the deadline back as there were many questions. To clarify, one design piece to be reused for three different products (sandwiches in this case) Same piece, but one for each sandwich.

I posted a file called Artsquare that now has each photo partnered with its title and description

Target Market(s)

hungry people looking for lunch

Industry/Entity Type

Promo

Requirements
Must have
• Attached Menu front page elements, of chalkboard, chalk font existing front colors.

```html
<!DOCTYPE html>
<html lang="en">
<head>
<meta charset="utf-8">
<title>Spicy Roast Beef Sandwich – Lunch Menu Promo</title>
<link href="https://fonts.googleapis.com/css2?family=Cabin+Sketch:wght@400;700&family=Crimson+Text:wght@600;700&display=swap" rel="stylesheet">
<style>
  :root {
    --chalkboard-dark: #1f1f1f;
    --chalkboard-mid: #3a3a3a;
    --frame-white: #ffffff;
    --tag-slate: #3b3d3b;
    --brand-orange: #f27a22;
    --chalk-white: #fbf7f0;
    --ink-dark: #2f2b28;
    --basil-green: #4f7a22;
    --roll-orange: #e0661c;
    --caption-veil: rgba(255, 255, 255, 0.72);
  }
  * { margin: 0; padding: 0; box-sizing: border-box; }
  html, body { width: 1200px; height: 1200px; overflow: hidden; }
  body {
    background: var(--chalkboard-dark);
    font-family: "Crimson Text", Georgia, serif;
  }
  .flyer {
    position: relative;
    width: 1200px;
    height: 1200px;
    background:
      radial-gradient(ellipse at 50% 45%, var(--chalkboard-mid) 0%, #2c2c2c 45%, var(--chalkboard-dark) 100%);
  }
  .photo-frame {
    position: absolute;
    left: 102px; top: 77px;
    width: 998px; height: 1059px;
    background: var(--frame-white);
    box-shadow: 0 6px 24px rgba(0,0,0,0.45);
  }
  .product-photo {
    position: absolute;
    left: 162px; top: 146px;
    width: 883px; height: 904px;
    background:
      linear-gradient(180deg,
        #d9a25e 0%, #e6b36b 18%, #f2e6c4 28%, #6f8a3a 34%,
        #cfd6b0 42%, #8a4a3c 55%, #b87a70 64%, #e2a860 78%, #f0c98a 100%);
  }
  .menu-tag {
    position: absolute;
    left: 30px; top: 225px;
    width: 304px; height: 154px;
    background: var(--tag-slate);
    box-shadow: 4px 6px 14px rgba(0,0,0,0.55);
    padding: 10px 20px 0 22px;
  }
  .menu-tag__title {
    font-family: "Cabin Sketch", cursive;
    font-weight: 400;
    font-size: 60px;
    letter-spacing: 6px;
    color: var(--brand-orange);
    line-height: 1;
    margin-left: 20px;
  }
  .menu-tag__brand {
    font-family: "Crimson Text", Georgia, serif;
    font-weight: 600;
    font-size: 40px;
    color: var(--chalk-white);
    line-height: 1;
    margin-top: 18px;
    white-space: nowrap;
  }
  .item-title {
    position: absolute;
    left: 661px; top: 425px;
    width: 491px; height: 168px;
    background: var(--brand-orange);
    box-shadow: 4px 6px 14px rgba(0,0,0,0.45);
    padding: 12px 14px 0 18px;
    font-family: "Cabin Sketch", cursive;
    font-weight: 400;
    font-size: 37px;
    line-height: 1.3;
    letter-spacing: 1px;
    text-transform: uppercase;
    color: var(--chalk-white);
  }
  .item-description {
    position: absolute;
    left: 48px; top: 764px;
    width: 575px; height: 152px;
    background: var(--caption-veil);
    padding: 16px 20px 0 136px;
    font-weight: 700;
    font-size: 28px;
    line-height: 1.3;
    color: var(--ink-dark);
  }
  .item-description .basil { color: var(--basil-green); }
  .item-description .roll { color: var(--roll-orange); }
</style>
</head>
<body>
  <main class="flyer">
    <div class="photo-frame"></div>
    <div class="product-photo" role="img" aria-label="Close-up photo of a spicy roast beef sandwich on a toasted ciabatta roll with melted cheese, basil, sprouts and onions"></div>

    <div class="menu-tag">
      <p class="menu-tag__title">MENU</p>
      <p class="menu-tag__brand">Noonday Bistro</p>
    </div>

    <h1 class="item-title">Spicy Roast Beef<br>Sandwich with Danish<br>Smelly Cheese</h1>

    <p class="item-description">
      Sprouts, <span class="basil">fresh basil</span>,<br>
      onions and Chili Sauce<br>
      on a <span class="roll">fresh Ciabatta Roll</span>
    </p>
  </main>
</body>
</html>
```